A private security company called "Ventrell Security Services Ltd"

Hello everybody,

We need a web page for a company based in NZ. It is mainly an informative website so it would be wonderful if the designer puts their absolute best into making it a website that I would really appreciate. The website needs to show professionalism and also needs to make our web surfers find the information they need in a click. the company's colour is black and silver, and if those two colours could be integrated into the website it would be absolutely lovely. Please do contact me for any information.

Sincerely,
Dorian Valcourt

```html
<!DOCTYPE html>
<html lang="en">
<head>
<meta charset="utf-8">
<title>Ventrell Security Services Ltd</title>
<link href="https://fonts.googleapis.com/css2?family=Lato:wght@400;700;900&family=Open+Sans:ital,wght@0,400;0,600;0,700;1,400&family=Tinos&display=swap" rel="stylesheet">
<style>
:root{
  --black:#0c0c0c;
  --ink:#2b2b2b;
  --text:#6a6a6a;
  --muted:#8a8a8a;
  --silver:#d9d9d9;
  --silver-light:#f1f1f1;
  --paper:#f7f7f7;
  --white:#ffffff;
  --line:#dedede;
  --hero-blue:#0f3c55;
  --hero-deep:#081822;
  --alarm-red:#b8141c;
}
*{margin:0;padding:0;box-sizing:border-box}
html,body{width:833px;height:1200px;overflow:hidden}
body{position:relative;background:var(--paper);font-family:"Open Sans",sans-serif;color:var(--text)}
.abs{position:absolute}

/* hero */
.hero{position:absolute;left:0;top:0;width:833px;height:358px;overflow:hidden;
  background:radial-gradient(circle at 52% 40%,#9a1018 0,#6a0d14 18%,transparent 34%),
  radial-gradient(circle at 22% 60%,#2c7a9a 0,transparent 30%),
  radial-gradient(circle at 92% 70%,#2d8fb8 0,transparent 28%),
  linear-gradient(135deg,var(--hero-deep),var(--hero-blue) 55%,var(--hero-deep))}
.side-nav{position:absolute;left:90px;top:0;width:140px;height:322px}
.side-nav svg{position:absolute;left:0;top:0}
.brand-block{position:absolute;left:0;top:44px;width:140px;text-align:center;color:var(--black)}
.brand-name{font-family:"Lato",sans-serif;font-weight:900;font-size:20px;letter-spacing:2px;line-height:1}
.brand-sub{font-family:"Lato",sans-serif;font-weight:700;font-size:7.4px;letter-spacing:.4px;margin-top:3px}
.brand-mark{width:16px;height:16px;border-radius:50%;background:var(--black);margin:0 auto 8px}
.nav-list{position:absolute;left:0;top:158px;width:140px;list-style:none;text-align:center}
.nav-list li{font-family:"Tinos",serif;font-size:13px;color:#333;height:26.5px;line-height:24px;
  border-bottom:1px solid #d4d4d4;margin:0 14px}
.nav-list li:last-child{border-bottom:none}

.promo{position:absolute;left:498px;top:0;width:268px;height:358px;
  background:linear-gradient(180deg,rgba(0,0,0,.82),rgba(0,0,0,.72));text-align:center;color:var(--white);
  border-left:1px solid rgba(255,255,255,.15);border-right:1px solid rgba(255,255,255,.15)}
.promo .brand-mark{background:var(--white);margin-top:20px;margin-bottom:6px}
.promo .brand-name{font-size:15px;letter-spacing:1.5px}
.promo .brand-sub{font-size:6px}
.promo h1{font-family:"Tinos",serif;font-weight:400;font-size:25px;line-height:27px;margin-top:16px}
.promo p{font-family:"Tinos",serif;font-size:13.5px;line-height:17.5px;letter-spacing:.4px;margin:16px 10px 0}
.promo .call{font-family:"Tinos",serif;font-size:12.5px;letter-spacing:.6px;margin-top:22px}
.promo .phone{font-family:"Open Sans",sans-serif;font-size:23px;margin-top:2px;display:flex;align-items:center;justify-content:center;gap:8px}
.thumbs{position:absolute;left:52px;top:300px;display:flex;gap:17px}
.thumb{width:43px;height:43px;border:1px solid #cfcfcf}
.thumb.active{border:2px solid #9fd6ee}

/* welcome */
.welcome{position:absolute;left:0;top:358px;width:833px;height:120px;background:var(--white);border-bottom:1px solid var(--line)}
.welcome h2{position:absolute;left:0;top:14px;width:833px;display:flex;justify-content:center;align-items:baseline;gap:10px;
  font-family:"Open Sans",sans-serif;font-weight:400;font-size:17px;color:var(--ink);letter-spacing:-.5px}
.welcome h2 .wm{font-family:"Lato",sans-serif;font-weight:900;font-size:16px;letter-spacing:1.5px;color:var(--black)}
.welcome .rule{position:absolute;left:316px;top:48px;width:200px;height:3px;border-radius:50%;
  background:radial-gradient(ellipse,rgba(0,0,0,.18),transparent 70%)}
.welcome p{position:absolute;left:96px;top:63px;width:650px;text-align:center;font-size:8.6px;line-height:15px;color:var(--text)}

/* section headers */
.bar{position:absolute;height:22px;border-radius:3px;background:linear-gradient(180deg,#3a3a3a,#050505);color:var(--white);
  font-family:"Open Sans",sans-serif;font-weight:700;font-size:12.5px;line-height:22px;padding-left:50px}
.badge{position:absolute;left:8px;top:-5px;width:34px;height:32px}
.pager{position:absolute;right:4px;top:3px;display:flex;gap:1px}
.pager span{width:19px;height:16px;background:linear-gradient(#fafafa,#cfcfcf);border-radius:2px;display:flex;align-items:center;justify-content:center}

.features{position:absolute;left:96px;top:534px;list-style:none;font-size:8.8px;color:var(--text)}
.features li{position:relative;padding-left:16px;height:23.2px;line-height:12px}
.features li svg{position:absolute;left:0;top:2px}

.service{position:absolute;top:535px;width:136px}
.service .photo{width:136px;height:63px}
.service h3{font-family:"Open Sans",sans-serif;font-weight:700;font-size:11.3px;color:var(--ink);margin-top:9px}
.service p{font-size:8.6px;line-height:11.6px;color:var(--text);margin-top:2px;width:132px}
.plus{position:absolute;width:12px;height:12px}

.divider{position:absolute;left:90px;top:684px;width:661px;height:1px;background:var(--line)}

/* boxes */
.box{position:absolute;top:702px;width:202px;height:172px;background:var(--white);border:1px solid #e6e6e6;border-radius:6px;
  box-shadow:0 3px 4px rgba(0,0,0,.06)}
.box h4{position:absolute;left:15px;top:12px;font-family:"Open Sans",sans-serif;font-size:13px;font-weight:700;color:var(--ink)}
.box h4 span{font-weight:600;color:#6a6a6a}
.box .hr{position:absolute;left:15px;right:15px;top:37px;border-top:1px dashed #d6d6d6}
.news{position:absolute;left:15px;width:180px;display:flex;gap:9px}
.date{width:29px;flex:none;text-align:center}
.date .m{background:#6b6b6b;color:var(--white);font-size:8px;font-weight:700;line-height:11px}
.date .d{background:#e4e4e4;color:#333;font-size:11.5px;font-weight:700;line-height:16px}
.news p{font-size:8.6px;line-height:14px;color:var(--text)}
.quote{position:absolute;left:15px;top:46px;width:172px;height:84px;background:#efefef;border-radius:5px;padding:7px 9px;
  font-style:italic;font-size:8.6px;line-height:13px;letter-spacing:.2px;color:var(--text)}
.quote-tail{position:absolute;left:30px;top:130px}
.cite{position:absolute;left:57px;top:137px;font-size:8px;font-weight:700;color:#555}
.field{position:absolute;left:15px;width:171px;background:var(--white);border:1px solid #bdbdbd;border-radius:3px;font-size:6.5px;color:#333;padding:3px 6px;
  box-shadow:inset 0 1px 2px rgba(0,0,0,.1)}
.submit{position:absolute;left:129px;top:140px;width:56px;height:18px;border:1px solid #bdbdbd;border-radius:3px;background:linear-gradient(#fafafa,#d2d2d2);
  font-size:9px;font-weight:700;color:#333;text-align:center;line-height:16px}

/* clients */
.clients{position:absolute;left:0;top:914px;width:833px;height:130px;border-top:1px solid var(--line)}
.clients h5{position:absolute;left:90px;top:9px;font-family:"Open Sans",sans-serif;font-size:13px;font-weight:700;color:var(--ink)}
.clients h5 span{font-weight:600;color:#555}
.clients .hr{position:absolute;left:90px;width:661px;top:34px;border-top:1px dashed #d6d6d6}
.client-row{position:absolute;left:90px;top:50px;width:661px;height:60px}
.client{position:absolute;top:0;height:60px;display:flex;align-items:center;justify-content:center;gap:6px;
  font-family:"Open Sans",sans-serif;font-weight:600;font-size:19px;color:#3a3a3a;border-right:1px solid #cfcfcf}
.client:last-child{border-right:none}
.client i{display:block;width:16px;height:16px;border-radius:50%;background:#3a3a3a}
.arrow{position:absolute;top:72px}

/* footer */
.footer-cap{position:absolute;left:0;top:1044px;width:833px;height:10px;background:#a8a8a8}
footer{position:absolute;left:0;top:1054px;width:833px;height:146px;background:var(--black);color:var(--white)}
footer h6{position:absolute;top:17px;font-family:"Open Sans",sans-serif;font-weight:400;font-size:12px;padding-bottom:6px;border-bottom:1px dashed #555}
.links{position:absolute;list-style:none;font-size:8.8px;line-height:18px;color:#ddd}
.links li::before{content:"›";margin-right:6px;color:#aaa}
.contact-line{position:absolute;left:276px;display:flex;gap:8px;font-size:8.6px;line-height:12px;color:#ddd}
.contact-line b{color:var(--white);font-weight:700}
.email-in{position:absolute;left:457px;top:79px;width:151px;height:18px;background:var(--white);border-radius:2px;font-size:7.5px;font-style:italic;color:#888;padding:4px 6px}
.subscribe{position:absolute;left:457px;top:106px;width:66px;height:18px;background:#d0d0d0;border-radius:2px;color:#111;font-size:8.6px;font-weight:700;text-align:center;line-height:18px}
.foot-brand{position:absolute;left:628px;top:20px;width:148px;text-align:center}
.foot-brand .brand-mark{background:var(--white);width:22px;height:22px;margin-bottom:10px}
.foot-brand .brand-name{font-size:19px}
.foot-brand .brand-sub{font-size:7.2px}
.copy{position:absolute;left:628px;top:104px;width:148px;text-align:center;font-size:8.3px;line-height:13px;color:#ddd}
</style>
</head>
<body>

<section class="hero">
  <div class="abs" style="left:0;top:0;width:833px;height:358px" role="img" aria-label="Photographic backdrop of digital padlocks over streams of hexadecimal code, blue with one red padlock"></div>

  <nav class="side-nav">
    <svg width="140" height="322" viewBox="0 0 140 322">
      <path d="M0 0H140V300L70 322L0 300Z" fill="#eeeeee"/>
      <path d="M0 0H140V110Q140 140 70 152Q0 140 0 110Z" fill="#ffffff"/>
      <path d="M0 110Q0 140 70 152Q140 140 140 110" fill="none" stroke="#dcdcdc"/>
    </svg>
    <div class="brand-block">
      <div class="brand-mark"></div>
      <div class="brand-name">VENTRELL</div>
      <div class="brand-sub">SECURITY SERVICES LTD.</div>
    </div>
    <ul class="nav-list">
      <li>Home</li><li>About us</li><li>Services</li><li>News</li><li>Contact Us</li>
    </ul>
  </nav>

  <div class="promo">
    <div class="brand-mark"></div>
    <div class="brand-name">VENTRELL</div>
    <div class="brand-sub">SECURITY SERVICES LTD.</div>
    <h1>Commercial<br>Security</h1>
    <p>workplace violence was the third leading cause of workplace deaths in Washington State.</p>
    <div class="call">Call Toll-Free</div>
    <div class="phone">
      <svg width="10" height="16" viewBox="0 0 10 16"><rect x="1" y="1" width="8" height="14" rx="1.5" fill="none" stroke="#fff" stroke-width="1.6"/><rect x="3.5" y="12" width="3" height="1.2" fill="#fff"/></svg>
      <span>0-123-456-789</span>
    </div>
    <div class="thumbs">
      <div class="thumb active" role="img" aria-label="Thumbnail of a red padlock on blue code" style="background:linear-gradient(135deg,#1a5d80,#b8141c)"></div>
      <div class="thumb" role="img" aria-label="Thumbnail of a businessman touching a security screen" style="background:linear-gradient(135deg,#d8d8d8,#3a3a3a)"></div>
      <div class="thumb" role="img" aria-label="Thumbnail of a padlock emblem above a network of people" style="background:linear-gradient(135deg,#2b5aa8,#c8d8f0)"></div>
    </div>
  </div>
</section>

<section class="welcome">
  <h2>Welcome to <span class="wm">VENTRELL <small style="font-size:8px;letter-spacing:.4px">SECURITY SERVICES LTD.</small></span></h2>
  <div class="rule"></div>
  <p>Lorem ipsum dolor sit amet, consectetuer adipiscing elit, sed diam nonummy nibh euismod tincidunt ut laoreet dolore magna aliquams erat volutpat. Ut wisi enim ad minim veniam, quis nostrud exerci tation ullamcorper suscipit lobortis nisl ut aliquip ex ea commodo ina consequat. Duis autem vel eum iriure dolor essem consequat, vel illum dolore eu feugiat nullaapd facilisis at vero eros et accumsan et iusto odio dignissim qui blandit</p>
</section>

<div class="bar" style="left:90px;top:496px;width:204px">
  <svg class="badge" viewBox="0 0 34 32"><path d="M2 2H32V18Q32 27 17 31Q2 27 2 18Z" fill="#f2f2f2" stroke="#bbb"/></svg>
  Discernible Differences!
</div>
<div class="bar" style="left:319px;top:496px;width:432px">
  <svg class="badge" viewBox="0 0 34 32"><path d="M2 2H32V18Q32 27 17 31Q2 27 2 18Z" fill="#f2f2f2" stroke="#bbb"/></svg>
  Our Services
  <div class="pager">
    <span><svg width="6" height="8"><path d="M5 1L1 4L5 7" fill="none" stroke="#777"/></svg></span>
    <span><svg width="6" height="8"><path d="M1 1L5 4L1 7" fill="none" stroke="#777"/></svg></span>
  </div>
</div>

<ul class="features">
  <li><svg width="8" height="8" viewBox="0 0 10 10"><path d="M5 0L6.2 3.6H10L7 5.8L8.1 9.5L5 7.3L1.9 9.5L3 5.8L0 3.6H3.8Z" fill="#777"/></svg>Personal Attention - Single Point of Contact</li>
  <li><svg width="8" height="8" viewBox="0 0 10 10"><path d="M5 0L6.2 3.6H10L7 5.8L8.1 9.5L5 7.3L1.9 9.5L3 5.8L0 3.6H3.8Z" fill="#777"/></svg>Convenience - Nationwide 24/7 Service</li>
  <li><svg width="8" height="8" viewBox="0 0 10 10"><path d="M5 0L6.2 3.6H10L7 5.8L8.1 9.5L5 7.3L1.9 9.5L3 5.8L0 3.6H3.8Z" fill="#777"/></svg>Highly Trained Personel</li>
  <li><svg width="8" height="8" viewBox="0 0 10 10"><path d="M5 0L6.2 3.6H10L7 5.8L8.1 9.5L5 7.3L1.9 9.5L3 5.8L0 3.6H3.8Z" fill="#777"/></svg>Management - Industry Experts</li>
  <li style="height:30px"><svg width="8" height="8" viewBox="0 0 10 10"><path d="M5 0L6.2 3.6H10L7 5.8L8.1 9.5L5 7.3L1.9 9.5L3 5.8L0 3.6H3.8Z" fill="#777"/></svg>Strong Financial Management -<br>Growth Company</li>
</ul>

<div class="service" style="left:318px">
  <div class="photo" role="img" aria-label="House behind a shield emblem" style="background:linear-gradient(135deg,#9fb8cf,#5c6b4c)"></div>
  <h3>Property Guards</h3>
  <p>Lorem ipsum dolor sit amet, nibh tetuer adipiascing elit, sed diam is nonummy nibh.</p>
</div>
<div class="service" style="left:467px">
  <div class="photo" role="img" aria-label="Businessman pressing a padlock icon over a world map" style="background:linear-gradient(135deg,#d0d0d0,#4a4a4a)"></div>
  <h3>Corporate Events Security</h3>
  <p>Lorem ipsum dolor sit amet, nibh tetuer adipiascing elit, sed diam is nonummy nibh.</p>
</div>
<div class="service" style="left:615px">
  <div class="photo" role="img" aria-label="Bodyguard with earpiece seen from behind" style="background:linear-gradient(135deg,#6d6d6d,#1e1e1e)"></div>
  <h3>Personal Bodyguard</h3>
  <p>Lorem ipsum dolor sit amet, nibh tetuer adipiascing elit, sed diam is nonummy nibh.</p>
</div>
<svg class="plus" style="left:441px;top:657px" viewBox="0 0 12 12"><circle cx="6" cy="6" r="5.5" fill="#9a9a9a"/><path d="M6 3V9M3 6H9" stroke="#fff" stroke-width="1.4"/></svg>
<svg class="plus" style="left:591px;top:657px" viewBox="0 0 12 12"><circle cx="6" cy="6" r="5.5" fill="#9a9a9a"/><path d="M6 3V9M3 6H9" stroke="#fff" stroke-width="1.4"/></svg>
<svg class="plus" style="left:738px;top:657px" viewBox="0 0 12 12"><circle cx="6" cy="6" r="5.5" fill="#9a9a9a"/><path d="M6 3V9M3 6H9" stroke="#fff" stroke-width="1.4"/></svg>

<div class="divider"></div>

<div class="box" style="left:90px">
  <h4><span>Latest</span> News</h4>
  <div class="hr"></div>
  <div class="news" style="top:46px">
    <div class="date"><div class="m">AUG</div><div class="d">12</div></div>
    <p>Lorem ipsum dolor sit amet, nibh tetuer adipiascing elit, sed diam is nonummy nibh.</p>
  </div>
  <div class="news" style="top:104px">
    <div class="date"><div class="m">AUG</div><div class="d">12</div></div>
    <p>Lorem ipsum dolor sit amet, nibh tetuer adipiascing elit, sed diam is nonummy nibh.</p>
  </div>
  <svg class="plus" style="left:176px;top:146px" viewBox="0 0 12 12"><circle cx="6" cy="6" r="5.5" fill="#9a9a9a"/><path d="M6 3V9M3 6H9" stroke="#fff" stroke-width="1.4"/></svg>
</div>

<div class="box" style="left:320px">
  <h4><span>Client</span> Testimonials</h4>
  <div class="hr"></div>
  <div class="quote"><b style="font-style:normal;color:#999">“</b> Ut wisi enim ad minim venia ,Lorem ipsum dolor sit amet, consec tetuer adipiscing elit, sed diam nonummy nibh euismod tincidunt ut laoreet dolore magna aliquam erat volutpat.</div>
  <svg class="quote-tail" width="18" height="10"><path d="M0 0H18L14 10Z" fill="#efefef"/></svg>
  <div class="cite">-Minim veniam</div>
  <svg class="plus" style="left:176px;top:146px" viewBox="0 0 12 12"><circle cx="6" cy="6" r="5.5" fill="#9a9a9a"/><path d="M6 3V9M3 6H9" stroke="#fff" stroke-width="1.4"/></svg>
</div>

<div class="box" style="left:549px">
  <h4><span>Quick</span> Contact</h4>
  <div class="hr"></div>
  <div class="field" style="top:45px;height:16px">Name</div>
  <div class="field" style="top:66px;height:16px">Email</div>
  <div class="field" style="top:88px;height:42px">Message</div>
  <div class="submit">Submit</div>
</div>

<section class="clients">
  <h5><span>Our</span> Esteemed Clients</h5>
  <div class="hr"></div>
  <svg class="arrow" style="left:76px" width="12" height="24"><path d="M11 1L2 12L11 23" fill="none" stroke="#c8c8c8" stroke-width="4"/></svg>
  <div class="client-row">
    <div class="client" style="left:0;width:92px;font-size:24px;color:#777">KESTON</div>
    <div class="client" style="left:92px;width:154px"><i></i>Brindlewick</div>
    <div class="client" style="left:246px;width:155px"><i></i>Holloway</div>
    <div class="client" style="left:401px;width:119px">Norvale</div>
    <div class="client" style="left:520px;width:141px"><i></i>ARDENT</div>
  </div>
  <svg class="arrow" style="left:753px" width="12" height="24"><path d="M1 1L10 12L1 23" fill="none" stroke="#c8c8c8" stroke-width="4"/></svg>
</section>

<div class="footer-cap"></div>
<footer>
  <h6 style="left:101px;width:140px">Quick Link</h6>
  <ul class="links" style="left:101px;top:45px"><li>Home</li><li>About</li><li>Services</li><li>News</li></ul>
  <ul class="links" style="left:183px;top:45px"><li>Apply Now</li><li>Contact Us</li></ul>

  <h6 style="left:276px;width:162px">Contact Information</h6>
  <div class="contact-line" style="top:50px">
    <svg width="9" height="12" viewBox="0 0 9 12"><path d="M4.5 0A4.2 4.2 0 0 0 0.3 4.2C0.3 7.5 4.5 12 4.5 12S8.7 7.5 8.7 4.2A4.2 4.2 0 0 0 4.5 0Z" fill="#fff"/><circle cx="4.5" cy="4.2" r="1.6" fill="#0c0c0c"/></svg>
    <div><b>Ventrell Security</b><br>Diam nonummy nibh,<br>euismo tincidunt ut laoreet</div>
  </div>
  <div class="contact-line" style="top:95px">
    <svg width="10" height="10" viewBox="0 0 10 10"><path d="M2 0.5L3.6 2.8L2.7 4Q3.7 6.2 6 7.3L7.2 6.4L9.5 8L8.3 9.6Q3.8 9.3 0.4 1.7Z" fill="#fff"/></svg>
    <span>123-456-7890</span>
  </div>
  <div class="contact-line" style="top:117px">
    <svg width="11" height="9" viewBox="0 0 11 9"><rect x="0.5" y="0.5" width="10" height="8" fill="#fff"/><path d="M0.5 0.5L5.5 5L10.5 0.5" fill="none" stroke="#0c0c0c"/></svg>
    <span>info@ventrellsecurity.com</span>
  </div>

  <h6 style="left:457px;width:151px">Newsletter Sign Up</h6>
  <div class="abs" style="left:456px;top:55px;width:160px;font-size:8.6px;line-height:12px;color:#ddd">Lorem ipsudolor sit coec adipiscing elitsite amet</div>
  <div class="email-in">Email Address</div>
  <div class="subscribe">SUBSCRIBE</div>

  <div class="foot-brand">
    <div class="brand-mark"></div>
    <div class="brand-name">VENTRELL</div>
    <div class="brand-sub">SECURITY SERVICES LTD.</div>
  </div>
  <div class="copy">© 2014 Ventrell Security.<br>All rights reserved</div>
</footer>

</body>
</html>
```